Disaster Recovery firm needs design for impactful Door Hanger flyer

We need the design for a 4.25X11 inch door hanger with die-cut included for the hanger. The hangers will be hung on the door medium to high net worth clientele's residential homes. They need to reference the event Hurricane Ondine and speak to the issues that people have resulting from the storm and the benefits of our service. We will provide the sales language and bullet points.

Target Market(s)

Residential homeowners

Font styles to use
Sans Serif

Colors
3277b5
ec1f27
cee9f5
cedeed

Requirements
Must have
• Photos that include visual references to hurricane damage,
bullet points to convey the benefits of the service,
call to action, & company & local office contact information
Nice to have
• Great graphic design with layers & topics
Should not have
• Pictures of money, promises of "cash" or "no risk" and certain other violations of written statutes& compliance

```html
<!DOCTYPE html>
<html lang="en">
<head>
<meta charset="utf-8">
<title>Harborline Claims Consulting – Door Hanger</title>
<link rel="stylesheet" href="https://fonts.googleapis.com/css2?family=Montserrat:wght@400;500;700;900&family=Oswald:wght@400;500;600&family=Roboto+Condensed:wght@400;700&family=Lato:wght@400&family=Roboto+Mono:wght@500&display=swap">
<style>
  :root{
    --backdrop:#b3b3b3;
    --red-deep:#7a1418;
    --red:#cc2229;
    --blue:#1e5478;
    --white:#ffffff;
    --ink:#111111;
  }
  *{box-sizing:border-box;margin:0;padding:0}
  html,body{width:1200px;height:1200px;overflow:hidden}
  body{background:var(--backdrop);position:relative;font-family:"Montserrat",sans-serif;color:var(--white)}
  .hanger{position:absolute;top:126px;width:361px;height:917px;overflow:hidden;
    background:linear-gradient(90deg,var(--red-deep) 0%,var(--red) 45%,var(--red) 55%,var(--red-deep) 100%);
    box-shadow:0 2px 6px rgba(0,0,0,.35)}
  .hanger--front{left:201px}
  .hanger--back{left:639px}
  .layer{position:absolute;left:0;top:0;width:361px;height:917px}
  .photo{position:absolute}
  .hanger--front .photo{left:0;top:380px;width:361px;height:370px;
    background:linear-gradient(180deg,#4d5566 0%,#7b8190 30%,#d9cc95 55%,#9e8f74 80%,#b8ab94 100%)}
  .hanger--back .photo{left:20px;top:667px;width:326px;height:150px;border-radius:30px 30px 0 0;
    background:linear-gradient(180deg,#55704a 0%,#8a8b7e 40%,#a69f8e 70%,#6f6a60 100%)}
  .abs{position:absolute;left:0;width:100%;text-align:center}
  .brand{position:absolute;display:flex;align-items:center;gap:8px}
  .brand__dot{width:22px;height:22px;border-radius:50%;background:var(--white);flex:none}
  .brand__name{font-weight:500;font-size:13px;letter-spacing:3px;line-height:1.15;color:var(--white)}
  .brand__name span{display:block;font-size:9px;letter-spacing:3px;text-align:center}
  .invite{top:330px;font-size:13px;letter-spacing:1px;font-weight:400}
  .event-title{top:350px;font-weight:900;font-size:42px;line-height:38px;letter-spacing:-1px}
  .join{top:738px;font-family:"Oswald",sans-serif;font-size:17px;font-weight:400}
  .join b{font-size:21px;font-weight:600}
  .call{top:758px;font-weight:700;font-size:26px;letter-spacing:1px}
  .office{font-family:"Lato",sans-serif;font-size:12.5px}
  .office svg{vertical-align:-1px;margin-right:3px}
  .address{font-family:"Lato",sans-serif;font-size:9.5px}
  .url{position:absolute;left:64px;top:870px;width:233px;height:25px;border-radius:13px;background:var(--white);
    color:var(--ink);font-family:"Roboto Mono",monospace;font-size:13px;letter-spacing:1px;display:flex;align-items:center;justify-content:center}
  .headline{top:322px;font-family:"Oswald",sans-serif;font-weight:500;font-size:19px;line-height:21px;text-shadow:0 1px 3px rgba(0,0,0,.4)}
  .benefits-pill{position:absolute;left:38px;top:396px;width:285px;height:23px;border-radius:12px;background:var(--white);
    color:var(--ink);font-weight:900;font-size:14px;letter-spacing:.5px;display:flex;align-items:center;justify-content:center}
  .benefit{position:absolute;left:47px;width:300px;font-family:"Roboto Condensed",sans-serif;font-size:10.3px;line-height:13.7px}
  .benefit__tick{position:absolute;left:-16px;top:0}
  .consult{top:803px;font-family:"Oswald",sans-serif;font-size:12px;line-height:15px}
  .phone{top:836px;font-weight:700;font-size:25px;letter-spacing:1px}
</style>
</head>
<body>

<!-- Front side -->
<section class="hanger hanger--front">
  <div class="photo" role="img" aria-label="Photo of a hurricane-damaged beachfront house with collapsed lower floor under a stormy sky"></div>
  <svg class="layer" viewBox="0 0 361 917" aria-hidden="true">
    <defs>
      <linearGradient id="redSweepA" x1="0" x2="1">
        <stop offset="0" stop-color="#7a1418"/><stop offset=".5" stop-color="#cc2229"/><stop offset="1" stop-color="#7a1418"/>
      </linearGradient>
    </defs>
    <path d="M0 370 H361 V405 Q185 505 0 412 Z" fill="url(#redSweepA)"/>
    <path d="M0 412 Q185 505 361 405 V411 Q185 513 0 418 Z" fill="#fff"/>
    <path d="M0 418 Q185 513 361 411 V415 Q185 526 0 427 Z" fill="#111"/>
    <path d="M0 725 Q180 660 361 725 V733 Q180 672 0 733 Z" fill="#cc2229"/>
    <path d="M0 733 Q180 672 361 733 V741 Q180 684 0 741 Z" fill="#fff"/>
    <path d="M0 741 Q180 684 361 741 V917 H0 Z" fill="#1e5478"/>
    <circle cx="180" cy="162" r="95" fill="#b3b3b3"/>
    <path d="M96 0 H107 L140 76 L131 79 Z" fill="#b3b3b3"/>
  </svg>

  <div class="brand" style="left:52px;top:275px">
    <div class="brand__dot"></div>
    <div class="brand__name">HARBORLINE CLAIMS<span>CONSULTING</span></div>
  </div>
  <p class="abs invite">INVITES ALL FOR THE EVENT</p>
  <h1 class="abs event-title">HURRICANE<br>ONDINE</h1>

  <p class="abs join">JOIN US FOR A <b>FREE</b> EVENT TO</p>
  <p class="abs call">CALL 850-555-0142</p>
  <p class="abs office" style="top:795px"><svg width="8" height="11" viewBox="0 0 8 11"><path d="M4 0a4 4 0 0 0-4 4c0 3 4 7 4 7s4-4 4-7a4 4 0 0 0-4-4zm0 5.5A1.5 1.5 0 1 1 4 2.5a1.5 1.5 0 0 1 0 3z" fill="#fff"/></svg>Gulf Coast Office</p>
  <p class="abs address" style="top:811px">4120 Seabreeze Parkway #210 Gulf Breeze, FL 32561</p>
  <p class="abs office" style="top:827px"><svg width="8" height="11" viewBox="0 0 8 11"><path d="M4 0a4 4 0 0 0-4 4c0 3 4 7 4 7s4-4 4-7a4 4 0 0 0-4-4zm0 5.5A1.5 1.5 0 1 1 4 2.5a1.5 1.5 0 0 1 0 3z" fill="#fff"/></svg>Florida Office</p>
  <p class="abs address" style="top:844px">7820 N. Palm Trail #104 Coconut Creek, FL 33066</p>
  <div class="url">www.harborline-claims.com</div>
</section>

<!-- Back side -->
<section class="hanger hanger--back">
  <div class="photo" role="img" aria-label="Photo of a street strewn with storm debris beside a damaged motel office sign"></div>
  <svg class="layer" viewBox="0 0 361 917" aria-hidden="true">
    <path d="M0 792 Q180 730 361 792 V800 Q180 741 0 800 Z" fill="#fff"/>
    <path d="M0 800 Q180 741 361 800 V917 H0 Z" fill="#1e5478"/>
    <circle cx="181" cy="161" r="95" fill="#b3b3b3"/>
    <path d="M249 0 H261 L225 78 L216 75 Z" fill="#b3b3b3"/>
  </svg>

  <div class="brand" style="left:58px;top:270px">
    <div class="brand__dot"></div>
    <div class="brand__name">HARBORLINE CLAIMS<span>CONSULTING</span></div>
  </div>
  <h2 class="abs headline">THIS EVENT SPEAKS TO THE ISSUES<br>ABOUT RESULTING FROM HURRICANE<br>AND WE ARE HELP YOU</h2>
  <div class="benefits-pill">BENEFITS OF OUR SERVICE</div>

  <p class="benefit" style="top:430px"><svg class="benefit__tick" width="13" height="12" viewBox="0 0 13 12"><path d="M1 6.5 L4.5 10.5 L12 1" stroke="#fff" stroke-width="2.2" fill="none"/></svg>Don't let it become one for your financial and personal situation. The claim adjusters are brought in from remote locations that are sometimes just part time adjusters, overburdened with claim assignments, or uniformed about local building codes.</p>
  <p class="benefit" style="top:499px"><svg class="benefit__tick" width="13" height="12" viewBox="0 0 13 12"><path d="M1 6.5 L4.5 10.5 L12 1" stroke="#fff" stroke-width="2.2" fill="none"/></svg>It can take weeks or months to have your claim investigated much less settled. There couldn't be a more necessary time to hire your own adjuster to ensure your claim is settled for the maximum benefits you are owed.</p>
  <p class="benefit" style="top:568px"><svg class="benefit__tick" width="13" height="12" viewBox="0 0 13 12"><path d="M1 6.5 L4.5 10.5 L12 1" stroke="#fff" stroke-width="2.2" fill="none"/></svg>If you have experienced hurricane damage, we can help. If your repairs did not cover what the insurance company sent, we can re-open your claim readjust it, and get you the money you deserve. No matter what sort of hurricane you may be dealing with having a public adjuster on your side during the discovery phase of your property loss can make all the difference in the world.</p>

  <p class="abs consult">CALL US FOR YOUR FREE CONSULTATION<br>ON HOW WE CAN HELP YOU.</p>
  <p class="abs phone">844.555.0199</p>
  <div class="url">www.harborline-claims.com</div>
</section>

</body>
</html>
```